Website Design for a "Talent Recruitment Agency"

We are looking for a website design for the website of our "Talent Recruitment Agency"; which is called "Crestway Hub".
Our recruitment website "Crestway Hub" will be focusing on: "Crestway Hub: Linking People & Firms in Switzerland"; which means our target audience is two-folded:
(i) TALENT - that is currently residing in- or outside of Switzerland, and is open for and interested in the "Swiss Job Market".
(ii) COMPANIES - that are looking for talent for specific job vacancies in Switzerland.
With our "Crestway Hub" approach we inted to focus on Membership & Partnership:
(a)"Membership"(TALENT)
and
(b)"Partnership"(COMPANIES)
Some of the competitor sites we like are:
• www.plimora42.dk
• www.qelvo.ch
• www.brandolix.ch/en
A sitemap example of our website is attached.
Also attached is a "Crestway Hub" logo in .eps format and one in .jpeg format.
We very much look forward to receive your creative ideas.
Best regards,
Crestway Hub
Crestway Hub: Linking People & Firms in Switzerland.
Website: crestwayhub.ch - Twitter: CrestwayHubCH
Target Market(s)
(i) TALENT (with around 0-10 years of working experience), currently residing in- or outside of Switzerland, but eligible to work in Switzerland.
(ii) COMPANIES (national or international) that are based in Switzerland.
Industry/Entity Type
Recruitment

```html
<!DOCTYPE html>
<html lang="en">
<head>
<meta charset="utf-8">
<title>Crestway Hub</title>
<link rel="stylesheet" href="https://fonts.googleapis.com/css2?family=Open+Sans:wght@400;600;700&family=PT+Sans+Narrow:wght@400;700&display=swap">
<style>
:root{
  --orange:#f2651f;
  --blue:#0a80d6;
  --blue-light:#1696e6;
  --blue-dark:#0670c0;
  --ink:#3f3f3f;
  --muted:#6a6a6a;
  --line:#e2e2e2;
  --row-alt:#ededed;
  --footer-top:#3a3b3d;
  --footer-bottom:#111214;
  --white:#ffffff;
}
*{box-sizing:border-box;margin:0;padding:0}
html,body{width:764px;height:1200px;overflow:hidden;background:var(--white)}
body{font-family:"Open Sans",Arial,sans-serif;color:var(--ink);position:relative}
.abs{position:absolute}

/* header */
.brand{left:56px;top:44px;display:flex;align-items:center;gap:10px}
.brand-dot{width:56px;height:50px;border-radius:50%;background:var(--blue)}
.brand-name{font-size:27px;font-weight:600;color:var(--orange);letter-spacing:-.2px}
.btn{top:20px;height:24px;width:72px;border-radius:12px;color:var(--white);font-size:12px;display:flex;align-items:center;justify-content:center}
.btn-register{left:460px;background:var(--orange)}
.btn-login{left:552px;background:linear-gradient(#5a5a5a,#2e2e2e)}
.lang{left:645px;top:21px;width:62px;height:22px;border:1px solid #cfcfcf;font-size:10px;display:flex;align-items:center;gap:6px;padding-left:6px;color:#444}
.lang-flag{width:12px;height:8px;background:#2a3f8f}
.lang-caret{margin-left:auto;margin-right:6px;border:4px solid transparent;border-top-color:#333;border-bottom:0}
.search{left:541px;top:66px;width:166px;height:22px;border:1px solid #cfcfcf;font-size:9px;color:#888;padding:5px 8px}
.search svg{position:absolute;right:6px;top:5px}

/* navigation */
.nav{left:0;top:110px;width:764px;height:38px;background:linear-gradient(var(--blue-light),var(--blue-dark));display:flex;padding-left:55px}
.nav a{color:var(--white);font-size:11px;font-weight:700;text-decoration:none;display:flex;align-items:center;justify-content:center;border-right:1px solid rgba(0,0,0,.15);height:38px}
.nav a:last-child{border-right:0}
.nav .active{background:var(--orange)}

/* hero */
.hero{left:0;top:148px;width:764px;height:349px;background:linear-gradient(90deg,#e9e6e1 0%,#f3f1ee 35%,#eceae7 60%,#e3e2e0 100%)}
.hero-kicker{left:398px;top:272px;font-family:"PT Sans Narrow",Arial,sans-serif;font-size:22px;color:#4a4a4a}
.hero-title{left:398px;top:305px;font-family:"PT Sans Narrow",Arial,sans-serif;font-size:43px;font-weight:700;color:#3d3d3d}

/* features */
.features{left:0;top:497px;width:764px;height:168px;background:var(--blue)}
.feature-badge{top:452px;width:100px;height:100px;border-radius:50%;background:var(--orange);border:3px solid var(--white);box-shadow:0 0 0 2px var(--orange);display:flex;align-items:center;justify-content:center}
.feature-title{top:564px;width:260px;text-align:center;color:var(--white);font-size:19px;font-weight:400}
.feature-text{top:596px;width:230px;text-align:center;color:var(--white);font-size:9.5px;line-height:15.5px;letter-spacing:.35px}

/* jobs */
.section-title{font-size:19px;color:var(--orange);font-weight:400}
.jobs{left:54px;top:731px;width:408px;height:197px;border:1px solid var(--line);border-radius:3px;overflow:hidden;box-shadow:0 1px 2px rgba(0,0,0,.08)}
.jobs table{width:100%;border-collapse:collapse;font-size:9.5px;color:var(--muted)}
.jobs th{font-weight:400;font-size:11px;color:#555;text-align:left;height:38px;padding-left:13px;background:linear-gradient(#fff,#f2f2f2);border-bottom:1px solid var(--line)}
.jobs td{padding-left:13px;height:52px;line-height:16px}
.jobs tr.alt td{background:var(--row-alt)}
.jobs tr.tall td{height:57px}

/* companies */
.partner{font-size:15px;font-weight:700;width:120px;text-align:center;white-space:nowrap}

/* footer */
.footer{left:0;top:977px;width:764px;height:223px;background:linear-gradient(var(--footer-top),var(--footer-bottom))}
.footer-col{top:1003px}
.footer-col h4{font-size:12.5px;font-weight:400;color:var(--white);margin-bottom:9px}
.footer-col li{list-style:none;font-size:9.5px;color:#e6e6e6;line-height:18.5px}
.contact li{display:flex;align-items:center;gap:9px;line-height:24.5px;font-size:10px}
.footer-rule{left:0;top:1146px;width:764px;height:1px;background:#2f3032}
.footer-bottom{top:1172px;font-size:8.5px;color:var(--white)}
.social{left:618px;top:1166px;display:flex;gap:5px}
.social span{width:18px;height:18px;border-radius:50%;background:#8a8b8d}
</style>
</head>
<body>

<header>
  <div class="abs brand"><span class="brand-dot"></span><span class="brand-name">Crestway Hub</span></div>
  <div class="abs btn btn-register">REGISTER</div>
  <div class="abs btn btn-login">LOGIN</div>
  <div class="abs lang"><span class="lang-flag"></span>Eng<span class="lang-caret"></span></div>
  <div class="abs search">Search..
    <svg width="10" height="10" viewBox="0 0 10 10"><circle cx="4" cy="4" r="3" fill="none" stroke="#888" stroke-width="1.2"/><line x1="6.2" y1="6.2" x2="9" y2="9" stroke="#888" stroke-width="1.4"/></svg>
  </div>
</header>

<nav class="abs nav">
  <a class="active" style="width:72px">HOME</a>
  <a style="width:106px">ABOUT US</a>
  <a style="width:86px">TALENT</a>
  <a style="width:115px">COMPANIES</a>
  <a style="width:75px">JOBS</a>
  <a style="width:91px">EVENTS</a>
  <a style="width:115px">CONTACT US</a>
</nav>

<section>
  <div class="abs hero" role="img" aria-label="Photo of a smiling young professional in a white shirt, seated in a bright office"></div>
  <div class="abs hero-kicker">DUS AUTM VEUM IRIURE DOOR</div>
  <div class="abs hero-title">CLAIS ESTIAM</div>
</section>

<section>
  <div class="abs features"></div>
  <div class="abs feature-badge" style="left:172px">
    <svg width="52" height="52" viewBox="0 0 52 52"><path d="M26 6 L46 15 L26 24 L6 15Z M6 18 L24 27 L24 48 L6 39Z M28 27 L46 18 L46 39 L28 48Z" fill="#fff"/></svg>
  </div>
  <div class="abs feature-badge" style="left:496px">
    <svg width="54" height="54" viewBox="0 0 54 54" fill="none" stroke="#fff" stroke-width="2"><circle cx="14" cy="14" r="5"/><circle cx="27" cy="11" r="5"/><circle cx="40" cy="14" r="5"/><path d="M8 44 V24 h12 V44 M21 44 V20 h12 V44 M34 44 V24 h12 V44"/></svg>
  </div>
  <h2 class="abs feature-title" style="left:92px">MEMBERSHIP</h2>
  <p class="abs feature-text" style="left:107px">Lorem ipsum dolor sit amet adipismsan morbi ut elit utipsum tristiquea Pellentesque habitant morbi Aenean massa.</p>
  <h2 class="abs feature-title" style="left:416px">PARTNERSHIP</h2>
  <p class="abs feature-text" style="left:431px">Lorem ipsum dolor sit amet adipismsan morbi ut elit utipsum tristiquea Pellentesque habitant morbi Aenean massa.</p>
</section>

<section>
  <h3 class="abs section-title" style="left:55px;top:686px">Latest Job Postings</h3>
  <div class="abs jobs">
    <table>
      <tr><th style="width:111px">Posted Date</th><th style="width:95px">Posistion</th><th style="width:99px">Company</th><th>Qualification</th></tr>
      <tr><td>Mar 08, 2011</td><td>Web Designer<br>/Developer</td><td>Com Resource<br>Management</td><td>Diploma</td></tr>
      <tr class="alt"><td>Mar 08, 2011</td><td>Web Designer<br>/Developer</td><td>Com Resource<br>Management</td><td>Diploma</td></tr>
      <tr class="tall"><td>Mar 08, 2011</td><td>Web Designer<br>/Developer</td><td>Com Resource<br>Management</td><td>Diploma</td></tr>
    </table>
  </div>

  <h3 class="abs section-title" style="left:527px;top:686px">Companies</h3>
  <div class="abs partner" style="left:500px;top:737px;color:#333">Kestrova</div>
  <div class="abs partner" style="left:612px;top:737px;color:#222">Pelmvark</div>
  <div class="abs partner" style="left:478px;top:789px;color:#111">Dravello</div>
  <div class="abs partner" style="left:598px;top:789px;color:#555">Quenly Home</div>
  <div class="abs partner" style="left:485px;top:846px;color:#e8312e">ujvo</div>
  <div class="abs partner" style="left:603px;top:846px;color:#555">Tarvish Food</div>
  <div class="abs partner" style="left:498px;top:902px;color:#2c3f8c">Ostrevi</div>
  <div class="abs partner" style="left:628px;top:902px;color:#1a2a4a">Brunaxel</div>
</section>

<footer>
  <div class="abs footer"></div>
  <div class="abs footer-col" style="left:56px"><h4>Quick Link</h4><ul><li>Typi non haben</li><li>Successful Campaigns</li><li>New Campaigns</li><li>Ending Soon</li><li>Most Funded Campaigns</li></ul></div>
  <div class="abs footer-col" style="left:217px"><h4>Services</h4><ul><li>Typi non haben</li><li>Successful Campaigns</li><li>New Campaigns</li><li>Ending Soon</li><li>Most Funded Campaigns</li></ul></div>
  <div class="abs footer-col" style="left:385px"><h4>Navigation</h4><ul><li>Typi non haben</li><li>Successful Campaigns</li><li>New Campaigns</li><li>Ending Soon</li><li>Most Funded Campaigns</li></ul></div>
  <div class="abs footer-col contact" style="left:575px"><h4>Contact</h4><ul>
    <li><svg width="10" height="10" viewBox="0 0 10 10"><path d="M2 0.5 L4 2.5 L3 4 Q4.5 6 6 7 L7.5 6 L9.5 8 L8 9.5 Q2 8.5 0.5 2Z" fill="#ddd"/></svg>+1 800 555 0142</li>
    <li><svg width="10" height="11" viewBox="0 0 10 11"><path d="M5 0.5 A3.8 3.8 0 0 1 8.8 4.3 C8.8 7 5 10.5 5 10.5 C5 10.5 1.2 7 1.2 4.3 A3.8 3.8 0 0 1 5 0.5Z" fill="#ddd"/><circle cx="5" cy="4.3" r="1.4" fill="#333"/></svg>4120. Harrow Lane Place,</li>
    <li><svg width="11" height="8" viewBox="0 0 11 8"><rect width="11" height="8" fill="#ddd"/><path d="M0 0 L5.5 4.5 L11 0" fill="none" stroke="#333" stroke-width="1"/></svg>hello@crestwayhub.ch</li>
  </ul></div>
  <div class="abs footer-rule"></div>
  <div class="abs footer-bottom" style="left:55px">Terms and Conditions | Disclaimer Plicy</div>
  <div class="abs footer-bottom" style="left:305px">Copyright © 2013. All Rights Reserved.</div>
  <div class="abs social"><span></span><span></span><span></span><span></span></div>
</footer>

</body>
</html>
```